11 x 17 Orvanthes Quote

Design the following quote in a poster.

"First say to yourself what you would be; then do what you have to do." - Orvanthes

See here for inspiration - https://prints.mornbrekal.com/

Quote

```html
<!DOCTYPE html>
<html lang="en">
<head>
<meta charset="utf-8">
<title>Orvanthes Quote Poster</title>
<link rel="stylesheet" href="https://fonts.googleapis.com/css2?family=Cinzel:wght@400;500&family=Libre+Baskerville:wght@700&display=swap">
<style>
  :root {
    --paper: #f1f1f1;
    --wash-green: #b9cdbb;
    --wash-grey: #dcdcdc;
    --band: #9bb5a0;
    --ink: #1b1b1b;
    --attribution: #7a1414;
  }
  html, body {
    margin: 0;
    padding: 0;
    overflow: hidden;
  }
  .poster {
    position: relative;
    width: 776px;
    height: 1200px;
    overflow: hidden;
    background: var(--paper);
  }
  .texture {
    position: absolute;
    inset: 0;
    background:
      radial-gradient(ellipse 260px 120px at 90px 80px, rgba(185,205,187,0.55), transparent 70%),
      radial-gradient(ellipse 220px 140px at 720px 300px, rgba(185,205,187,0.45), transparent 70%),
      radial-gradient(ellipse 300px 160px at 80px 720px, rgba(185,205,187,0.45), transparent 70%),
      radial-gradient(ellipse 240px 120px at 520px 1050px, rgba(185,205,187,0.35), transparent 70%),
      radial-gradient(ellipse 320px 200px at 650px 620px, rgba(220,220,220,0.7), transparent 70%),
      radial-gradient(ellipse 300px 180px at 200px 1000px, rgba(210,210,210,0.6), transparent 70%),
      linear-gradient(160deg, #eef0ee 0%, #f4f4f4 50%, #ececec 100%);
  }
  .quote {
    margin: 0;
    position: absolute;
    inset: 0;
    font-family: "Cinzel", "Trajan Pro", serif;
    font-weight: 400;
    color: var(--ink);
  }
  .quote-line {
    position: absolute;
    height: 78px;
    line-height: 80px;
    background: var(--band);
    text-align: center;
    font-size: 60px;
    letter-spacing: 1px;
    white-space: nowrap;
  }
  .line-1 { left: 260px; top: 288px; width: 266px; }
  .line-2 { left: 60px;  top: 371px; width: 666px; }
  .line-3 { left: 157px; top: 454px; width: 472px; }
  .line-4 { left: 157px; top: 538px; width: 472px; }
  .line-5 { left: 187px; top: 621px; width: 411px; }
  .line-6 { left: 157px; top: 704px; width: 472px; }
  .line-7 { left: 107px; top: 787px; width: 556px; }
  .attribution {
    position: absolute;
    left: 0;
    top: 914px;
    width: 776px;
    text-align: center;
    font-family: "Libre Baskerville", "Baskerville", serif;
    font-weight: 700;
    font-size: 25px;
    color: var(--attribution);
  }
</style>
</head>
<body>
  <main class="poster">
    <div class="texture" role="img" aria-label="Soft painted brushstroke texture in pale sage green and light grey"></div>
    <blockquote class="quote">
      <span class="quote-line line-1">"First</span>
      <span class="quote-line line-2">Say to yourself</span>
      <span class="quote-line line-3">What you</span>
      <span class="quote-line line-4">would be;</span>
      <span class="quote-line line-5">then do</span>
      <span class="quote-line line-6">What you</span>
      <span class="quote-line line-7">have to do."</span>
    </blockquote>
    <p class="attribution">Orvanthes</p>
  </main>
</body>
</html>
```